Land Development Company Website Redesign

We are looking for a fresh design for our website. The content will remain 90% the same.

We really like the layout style of www.quibbenstor.com.

We have attached our current site for content.

Industry/Entity Type

Real Estate Development

Coding

Coded - Design and coding required

Number of Pages Required

5+ page

Font styles to use
Sans Serif

Requirements
Must have
• Consistent feel across all the pages. Visually appealing and simple layout design that can be viewed on a mobile device and browser.

```html
<!DOCTYPE html>
<html lang="en">
<head>
<meta charset="utf-8">
<title>Cedar Ridge Estates</title>
<link href="https://fonts.googleapis.com/css2?family=Roboto:wght@300;400;500;700&family=Roboto+Condensed:wght@400;700&display=swap" rel="stylesheet">
<style>
:root{
  --gold:#c8a96a;
  --gold-dark:#a98a4e;
  --gold-soft:#e9dcc0;
  --ink:#333333;
  --text:#666666;
  --page:#f7f7f5;
  --white:#ffffff;
  --dark:#2e2e2e;
}
*{box-sizing:border-box;margin:0;padding:0}
html,body{width:1200px;height:2552px;overflow:hidden}
body{background:var(--page);font-family:"Roboto",Arial,sans-serif;color:var(--text);position:relative}
.hero{position:absolute;left:0;top:0;width:1200px;height:645px}
.hero-photo{position:absolute;inset:0;background:linear-gradient(180deg,#b7a9c9 0%,#c9b9c4 25%,#8c8070 55%,#4f5a3a 80%,#3c4a2c 100%)}
.brand-name{position:absolute;left:0;right:0;top:84px;text-align:center;font-family:"Roboto Condensed",sans-serif;font-weight:700;font-size:26px;letter-spacing:4px;color:var(--white)}
.nav{position:absolute;left:0;top:590px;width:1200px;height:55px;background:var(--gold);display:flex;align-items:center;padding:0 88px}
.nav ul{list-style:none;display:flex;margin-left:230px}
.nav li{font-family:"Roboto Condensed",sans-serif;color:var(--white);font-size:15px;padding:0 20px;line-height:55px}
.nav li.active{background:var(--gold-dark)}
.search{margin-left:auto;width:210px;height:32px;background:var(--white);display:flex;align-items:center;justify-content:space-between;padding:0 10px;font-size:13px;color:#aaa}
.section-title{font-family:"Roboto Condensed",sans-serif;font-size:44px;font-weight:700;color:var(--ink);text-align:center}
.section-title em{font-style:normal;color:var(--gold)}
.welcome{position:absolute;left:0;top:645px;width:1200px;height:355px;text-align:center}
.welcome .section-title{margin-top:80px}
.welcome p{width:860px;margin:24px auto 0;font-size:15px;line-height:24px;color:var(--text)}
.btn-more{display:inline-block;margin-top:28px;height:46px;line-height:46px;padding:0 26px;background:var(--dark);color:var(--white);font-weight:500;font-size:14px;letter-spacing:1px}
.location{position:absolute;left:0;top:1000px;width:1200px;height:480px}
.location-photo{position:absolute;inset:0;background:linear-gradient(180deg,#6e8a4f 0%,#9fb48a 35%,#8c8a7e 60%,#5f7a3c 100%)}
.location h2{position:absolute;left:0;right:0;top:210px;text-align:center;font-family:"Roboto Condensed",sans-serif;font-weight:400;font-size:46px;color:var(--white)}
.gallery{position:absolute;left:0;top:1480px;width:1200px;height:660px}
.gallery .section-title{margin-top:70px}
.grid{position:absolute;left:88px;top:180px;width:1024px;height:376px;display:grid;grid-template-columns:repeat(4,1fr);grid-template-rows:1fr 1fr;gap:8px}
.tile{position:relative}
.tile.stairs{grid-row:1/3;background:linear-gradient(160deg,#efe9e2,#c9a98a 60%,#8c6a4a)}
.tile.villa{background:linear-gradient(160deg,#4a5260,#283040)}
.tile.villa span{position:absolute;left:20px;top:20px;color:var(--white);font-size:15px}
.tile.house{grid-column:3/5;background:linear-gradient(180deg,#2a4670,#8aa0b8 55%,#5c6a4a)}
.tile.living{background:linear-gradient(160deg,#e4e6e8,#9ea4a8)}
.tile.lounge{background:linear-gradient(160deg,#d9c3a8,#8a6e52)}
.tile.room{background:linear-gradient(160deg,#f0ece6,#c45a3a 70%,#7a4a30)}
.tabs{position:absolute;left:0;right:0;top:590px;display:flex;justify-content:center;gap:34px;font-size:13px;color:var(--text)}
.tabs span.active{color:var(--ink);border-bottom:2px solid var(--gold);padding-bottom:6px}
.offer{position:absolute;left:0;top:2140px;width:1200px;height:150px;background:var(--gold-soft);display:flex;align-items:center;padding:0 88px}
.offer h3{font-family:"Roboto Condensed",sans-serif;font-size:30px;font-weight:700;color:var(--ink)}
.offer p{font-size:15px;margin-top:8px;color:var(--ink)}
.btn-book{margin-left:auto;border:2px solid var(--ink);padding:12px 24px;font-weight:500;font-size:14px;color:var(--ink)}
.footer{position:absolute;left:0;top:2290px;width:1200px;height:222px;background:var(--white);padding:30px 88px 0;display:grid;grid-template-columns:360px 330px 1fr;gap:20px}
.footer h4{color:var(--gold);font-weight:400;font-size:18px;margin-bottom:14px}
.footer li{list-style:none;font-size:13px;line-height:26px;color:var(--text)}
.footer li strong{color:var(--ink)}
.hours li{position:relative;padding-left:18px}
.hours li:before{content:"";position:absolute;left:0;top:10px;width:6px;height:6px;border-radius:50%;background:var(--gold)}
.newsletter p{font-size:13px;line-height:22px}
.subscribe{display:flex;margin-top:18px;height:40px;width:330px}
.subscribe span{flex:1;border:1px solid #ddd;font-size:13px;color:#aaa;padding:0 12px;line-height:38px}
.subscribe b{width:44px;background:var(--gold);display:flex;align-items:center;justify-content:center}
.bottom{position:absolute;left:0;top:2512px;width:1200px;height:40px;background:var(--page);border-top:1px solid #e2e2e2;display:flex;align-items:center;padding:0 88px;font-size:12px}
.bottom strong{color:var(--ink);margin:0 4px}
.social{margin-left:auto;display:flex;gap:12px}
.social i{width:18px;height:18px;border-radius:50%;background:#999}
.social i.top{border-radius:0;background:var(--gold)}
</style>
</head>
<body>
<header class="hero">
  <div class="hero-photo" role="img" aria-label="Stone manor house with lit windows at dusk, lawn and trees in front"></div>
  <div class="brand-name">CEDAR RIDGE</div>
  <nav class="nav">
    <ul>
      <li class="active">Home</li><li>What's New</li><li>The Estates</li><li>The Team</li><li>Gallery</li><li>Contact</li>
    </ul>
    <div class="search">Search here
      <svg width="14" height="14" viewBox="0 0 14 14"><circle cx="6" cy="6" r="4.5" fill="none" stroke="#c8a96a" stroke-width="2"/><line x1="9.5" y1="9.5" x2="13" y2="13" stroke="#c8a96a" stroke-width="2"/></svg>
    </div>
  </nav>
</header>

<section class="welcome">
  <h1 class="section-title">Welcome to <em>CEDAR RIDGE ESTATES</em></h1>
  <p>Lorem Ipsum is simply dummy text of the printing and typesetting industry. Lorem Ipsum has been the industry's standard dummy text ever since the 1500s, when an unknown printer took a galley of type and scrambled it to make a type specimen book. It has survived not only five centuries, but also the leap into electronic typesetting, remaining essentially unchanged. It was popularised in the 1960s with the release of Letraset sheets containing Lorem Ipsum passages.</p>
  <div class="btn-more">READ MORE</div>
</section>

<section class="location">
  <div class="location-photo" role="img" aria-label="Family home with veranda behind a green lawn and a flowering purple tree"></div>
  <h2>ABC Main Street, Cedar Ridge</h2>
</section>

<section class="gallery">
  <h2 class="section-title">Welcome to <em>CEDAR RIDGE ESTATES</em></h2>
  <div class="grid">
    <div class="tile stairs" role="img" aria-label="Bright interior with floating wooden staircase"></div>
    <div class="tile villa" role="img" aria-label="Modern villa exterior at night"><span>Villa in Vegas</span></div>
    <div class="tile house" role="img" aria-label="Contemporary house with pool under a blue evening sky"></div>
    <div class="tile living" role="img" aria-label="Minimal white living room"></div>
    <div class="tile lounge" role="img" aria-label="Warm lounge with modern furniture"></div>
    <div class="tile room" role="img" aria-label="Bright bedroom with red accents"></div>
  </div>
  <div class="tabs"><span class="active">Luxury Homes</span><span>Luxury Amenities</span><span>Community</span><span>All</span></div>
</section>

<section class="offer">
  <div>
    <h3>HURRY ONLY THREE CUSTOM LOTS ARE AVAILABLE!</h3>
    <p>Lorem Ipsum is simply dummy text of the printing</p>
  </div>
  <div class="btn-book">BOOK NOW</div>
</section>

<footer class="footer">
  <div>
    <h4>Contact Info</h4>
    <ul>
      <li><strong>ADDRESS :</strong> 2210 N. Larkspur Lane, Fenwick, CA 90000</li>
      <li><strong>PHONE :</strong> (555) 410-2281</li>
      <li><strong>FAX :</strong> (555) 410-2290</li>
      <li><strong>E-MAIL :</strong> info@cedarridgeestates.com</li>
    </ul>
  </div>
  <div class="hours">
    <h4>Working Hours</h4>
    <ul>
      <li>Thursday 10-5:00</li><li>Friday 10-5:00</li><li>Saturday 10-5:00</li><li>Sunday 11-5:00</li>
    </ul>
  </div>
  <div class="newsletter">
    <h4>Newsletter</h4>
    <p>Lorem Ipsum is simply dummy text of the printing and typesetting industry.</p>
    <div class="subscribe"><span>Enter Your E-Mail</span><b><svg width="16" height="16" viewBox="0 0 16 16"><path d="M1 8 L15 1 L11 15 L8 9 Z" fill="#fff"/></svg></b></div>
  </div>
</footer>

<div class="bottom">© 2016 <strong>CEDAR RIDGE.</strong> All Rights Reserved
  <div class="social"><i></i><i></i><i></i><i></i><i></i><i class="top"></i></div>
</div>
</body>
</html>
```